Enhance Landing Page

Actual: https://thecoralparlor.com/aposte-em-solaria-lp-port/

I need a better design for this page:
Using this shortcodes : https://sturdy.qvxlayouts.net
Rules:
. Keep the page header
. Keep the footer

```html
<!DOCTYPE html>
<html lang="pt-BR">
<head>
<meta charset="utf-8">
<title>The Coral Parlor — Invista na Florida</title>
<link rel="stylesheet" href="https://fonts.googleapis.com/css2?family=Montserrat:wght@400;600;700;800&family=Open+Sans:wght@400;600;700&display=swap">
<style>
:root{
  --purple:#4b2a7d;
  --purple-dark:#3a2064;
  --navy:#2e2b63;
  --orange:#f7941d;
  --green:#2db742;
  --red:#e3173e;
  --pink:#e0287a;
  --teal:#23a9b8;
  --blue:#0f3d7a;
  --ink:#222;
  --muted:#666;
  --light:#efefef;
  --charcoal:#232323;
  --white:#fff;
}
*{box-sizing:border-box;margin:0;padding:0}
html,body{width:1200px;height:4959px;overflow:hidden}
body{font-family:"Open Sans",Arial,sans-serif;color:var(--ink);background:var(--white);position:relative}
.abs{position:absolute}
.brand{font-family:"Montserrat",Arial,sans-serif;font-weight:800;color:var(--purple);text-align:center;letter-spacing:2px;line-height:1}
.brand span{display:block}
.pill{display:inline-flex;align-items:center;justify-content:center;border-radius:30px;font-family:"Montserrat",Arial,sans-serif;font-weight:700;color:var(--white);white-space:nowrap}
.cta{display:flex;align-items:center;gap:8px;font-family:"Montserrat",Arial,sans-serif;font-weight:700;font-size:12px;line-height:1.2}
.cta i{width:34px;height:34px;border-radius:50%;display:inline-block;flex:none}
.phone-row{display:flex;align-items:center;gap:5px;font-size:10px;color:#333}
.phone-row i{width:10px;height:10px;border-radius:50%;background:#2a8c4a;display:inline-block}
.phone-row i.us{background:#3a4ea0}

/* header */
.site-header{left:0;top:0;width:1200px;height:83px;background:var(--white)}
.chat-badge{background:var(--green);font-size:11px;padding:4px 12px;border-radius:4px}

/* hero */
.hero{left:0;top:83px;width:1200px;height:628px;overflow:hidden;background:linear-gradient(180deg,#8cb8df 0%,#cfe2ee 28%,#7fa85a 50%,#4f8a2f 75%,#3f7a26 100%)}
.hero h1{position:absolute;top:160px;left:0;width:100%;text-align:center;font-family:"Montserrat",Arial,sans-serif;font-weight:800;font-size:44px;line-height:1.12;color:var(--white);text-shadow:0 2px 8px rgba(0,0,0,.35)}
.hero .tag{position:absolute;left:360px;top:300px;width:480px;height:38px;background:var(--red);font-size:13px;border-radius:4px}

/* presence */
.presence-photo{left:99px;top:803px;width:595px;height:215px;background:linear-gradient(135deg,#c9c2b4,#7a7066 55%,#4d463f)}
.presence h2{font-family:"Montserrat",Arial,sans-serif;font-weight:700;font-size:22px;color:var(--red);border-left:5px solid var(--red);padding-left:10px}
.presence p{font-size:11.5px;line-height:1.6;color:var(--muted);margin-bottom:12px}
.contact-box{left:711px;top:803px;width:390px;height:427px;background:var(--purple);padding:36px 26px;color:var(--white)}
.contact-box h3{text-align:center;font-family:"Montserrat",Arial,sans-serif;font-weight:600;font-size:18px;letter-spacing:1px;border-bottom:1px solid rgba(255,255,255,.3);padding-bottom:14px}
.contact-box .call{text-align:center;font-size:10px;margin:14px 0 16px;line-height:1.5}
.field{background:var(--white);border-radius:2px;font-size:10px;color:#888;padding:8px 8px}
.send{background:var(--orange);height:48px;border-radius:3px;font-size:15px;margin-top:18px;width:100%}

/* vision */
.vision-text{left:130px;top:1370px;width:465px;text-align:center}
.vision-text h2{font-family:"Montserrat",Arial,sans-serif;font-weight:800;font-size:38px;color:var(--purple)}
.vision-text h4{font-size:13.5px;font-weight:600;margin:14px 60px 18px;line-height:1.4}
.vision-text p{text-align:left;font-size:12px;line-height:1.6;color:var(--muted)}
.vision-btn{left:130px;top:1685px;width:460px;height:50px;background:var(--green);font-size:16px;border-radius:4px;gap:12px}
.services{left:600px;top:1306px;width:600px;height:480px;background:var(--navy);display:grid;grid-template-columns:repeat(4,1fr);grid-template-rows:repeat(2,1fr)}
.service{border-right:1px solid rgba(255,255,255,.12);border-bottom:1px solid rgba(255,255,255,.12);display:flex;flex-direction:column;align-items:center;justify-content:center;gap:14px;color:var(--white);font-family:"Montserrat",Arial,sans-serif;font-weight:700;font-size:12px;text-align:center;line-height:1.3}
.service svg{width:54px;height:54px}

/* specialist band */
.specialist{left:0;top:1792px;width:1200px;height:208px;background:linear-gradient(180deg,#1c1c1c,#3a3a3a 60%,#262626)}
.specialist h2{position:absolute;top:52px;width:100%;text-align:center;font-family:"Montserrat",Arial,sans-serif;font-weight:800;font-size:34px;color:var(--white)}
.specialist .pill{position:absolute;left:410px;top:110px;width:380px;height:50px;background:var(--orange);border-radius:3px;font-size:17px}

/* gallery */
.section-title{width:100%;text-align:center;font-family:"Montserrat",Arial,sans-serif;font-weight:700;font-size:38px;color:var(--ink)}
.gallery{left:24px;top:2165px;width:1152px;height:976px;display:grid;grid-template-columns:repeat(4,1fr);grid-template-rows:repeat(4,1fr);gap:12px}
.tile{border-radius:1px}
.load-more{left:530px;top:3190px;width:140px;height:36px;background:var(--purple-dark);font-size:11px;letter-spacing:1px}

/* plans */
.plans{left:0;top:3257px;width:1200px;height:264px;background:var(--blue);text-align:center;color:var(--white)}
.plans h2{margin-top:58px;font-family:"Montserrat",Arial,sans-serif;font-weight:800;font-size:29px}
.plans p{font-size:14px;line-height:1.6;margin-top:14px}
.plans .pill{margin-top:20px;width:160px;height:36px;background:var(--white);color:var(--red);font-size:12px}

/* builder */
.builder-photo{left:0;top:3531px;width:600px;height:463px;background:linear-gradient(160deg,#2a2a2a,#3d3d3d 50%,#1a1a1a)}
.builder-side{left:600px;top:3531px;width:600px;height:463px;background:var(--light)}
.builder-text{left:250px;top:3655px;width:290px;color:var(--white)}
.builder-text h2{font-family:"Montserrat",Arial,sans-serif;font-weight:800;font-size:30px;color:var(--orange);margin-bottom:12px}
.builder-text p{font-size:12px;line-height:1.55}
.stats{left:552px;top:3554px;width:588px;height:413px;background:var(--white);box-shadow:0 4px 20px rgba(0,0,0,.12);display:grid;grid-template-columns:1fr 1fr;grid-template-rows:1fr 1fr}
.stat{display:flex;flex-direction:column;align-items:center;justify-content:center;font-family:"Montserrat",Arial,sans-serif;font-weight:800;font-size:30px;line-height:1.2;text-align:center;color:var(--ink)}
.stat small{font-size:14px;font-weight:600}
.stat:nth-child(1),.stat:nth-child(3){border-right:1px solid #ddd}
.stat:nth-child(1),.stat:nth-child(2){border-bottom:1px solid #ddd}

/* contact form */
.help{left:0;top:4060px;width:1200px;text-align:center}
.help h3{font-family:"Montserrat",Arial,sans-serif;font-weight:400;font-size:26px;color:var(--ink)}
.help h2{font-family:"Montserrat",Arial,sans-serif;font-weight:800;font-size:42px;color:var(--purple);margin-top:4px}
.help p{font-size:13px;color:#888;letter-spacing:1px;margin-top:10px}
.input{border:1px solid #c9b8e6;font-size:12px;color:#999;padding:16px 14px;background:var(--white)}
.submit{left:258px;top:4486px;width:684px;height:54px;background:var(--purple-dark);border-radius:0;font-size:15px;letter-spacing:1px}

/* footer */
.site-footer{left:0;top:4612px;width:1200px;height:297px;background:linear-gradient(180deg,#f5f5f5,#e6e6e6)}
.addr{font-size:11px;line-height:1.5;color:#444}
.addr b{color:var(--ink);font-size:13px}
.legal{left:0;top:4909px;width:1200px;height:50px;background:#111;color:#ccc;font-size:10px;display:flex;align-items:center;justify-content:space-between;padding:0 60px}
.legal nav{display:flex;gap:40px;font-family:"Montserrat",Arial,sans-serif;font-weight:600;color:var(--white)}
</style>
</head>
<body>

<header class="site-header abs">
  <div class="abs" style="left:125px;top:10px">
    <div class="pill chat-badge">ChatLine +1 (555)010-4471</div>
    <div style="display:flex;gap:14px;margin-top:8px">
      <div class="phone-row"><i></i>+55 21 0000-4412</div>
      <div class="phone-row"><i class="us"></i>+1 (555)010-2298</div>
    </div>
  </div>
  <div class="brand abs" style="left:525px;top:12px;width:150px">
    <span style="font-size:24px">CORAL</span>
    <span style="font-size:13px;letter-spacing:5px;margin-top:4px">PARLOR</span>
  </div>
  <div class="cta abs" style="left:780px;top:22px"><i style="background:var(--pink)"></i>FALE COM UM<br>AGENTE</div>
  <div class="cta abs" style="left:935px;top:22px"><i style="background:var(--teal)"></i>AGENDE UMA<br>CONVERSA</div>
</header>

<section class="hero abs" role="img" aria-label="Golfista em campo verde sob céu ensolarado, com casas ao fundo">
  <h1>INVISTA NA FLORIDA<br>E RENTABILIZE TRANQUILIDADE</h1>
  <div class="pill tag">Conheça as melhores oportunidades de investimentos na florida</div>
  <svg class="abs" style="left:0;top:470px" width="1200" height="158" viewBox="0 0 1200 158">
    <path d="M0 20 Q600 175 1200 20 L1200 158 L0 158Z" fill="var(--red)"/>
    <path d="M0 45 Q600 190 1200 45 L1200 158 L0 158Z" fill="var(--white)"/>
    <circle cx="600" cy="118" r="5" fill="none" stroke="#bbb" stroke-width="1.5"/>
  </svg>
</section>

<section class="presence">
  <div class="presence-photo abs" role="img" aria-label="Sala de estar moderna com sofás e janelas amplas"></div>
  <div class="abs" style="left:99px;top:1035px;width:595px">
    <h2>Presentes no Brasil e Estados Unidos</h2>
    <div style="margin-top:18px">
      <p>O The Coral Parlor possui um Lounge permanente no Rio de Janeiro, Brasil e em Orlando, na Florida. Com um conceito inovador de atendimento 360º, assessorando os clientes que desejam comprar um imóvel nos Estados Unidos, seja para investir ou Morar.</p>
      <p>Com a parceria exclusiva da Halvorsen Homes, a maior construtora dos Estados Unidos, garantimos as melhores escolhas para você e sua família! Nossos especialistas possuem visão 360º para apoiar tudo em todo o processo e viver a melhor experiência na compra de um imóvel na América.</p>
    </div>
  </div>
  <form class="contact-box abs">
    <h3>FALE CONOSCO</h3>
    <div class="call"><b>LIGUE AGORA</b><br>+1 (555)010-2298 &nbsp;|&nbsp; +55 (21) 0000-4412</div>
    <div style="display:grid;grid-template-columns:1fr 1fr;gap:12px">
      <div style="display:flex;flex-direction:column;gap:12px">
        <div class="field">Seu nome</div>
        <div class="field">Seu E-Mail</div>
        <div class="field">Telefone</div>
      </div>
      <div class="field" style="height:104px">Sua Mensagem</div>
    </div>
    <div class="pill send">ENVIAR AGORA!</div>
  </form>
</section>

<section class="vision">
  <div class="vision-text abs">
    <h2>VISÃO 360º</h2>
    <h4>Cuidamos de absolutamente tudo para você se sentir em casa na Florida!</h4>
    <p>Atendimento 360º de brasileiro para brasileiro. Nossos especialistas irão lhe auxiliar em tudo o que você precisar para concretizar seu sonho de investir ou viver na América, com todo conforto e principalmente segurança. Desde a escolha do melhor imóvel até abertura de empresas e remessas financeiras.</p>
  </div>
  <div class="pill vision-btn abs">DESEJA FALAR VIA CHATLINE? <span style="width:22px;height:22px;border-radius:50%;background:var(--white);display:inline-block"></span></div>
  <div class="services abs">
    <div class="service"><svg viewBox="0 0 54 54"><rect x="6" y="14" width="42" height="26" rx="2" fill="none" stroke="#fff" stroke-width="3"/><circle cx="27" cy="27" r="7" fill="#fff"/></svg>FINANCIAMENTO</div>
    <div class="service"><svg viewBox="0 0 54 54"><rect x="12" y="6" width="30" height="42" rx="2" fill="#fff"/><circle cx="27" cy="22" r="6" fill="var(--navy)"/><rect x="18" y="32" width="18" height="8" fill="var(--navy)"/></svg>VISTOS</div>
    <div class="service"><svg viewBox="0 0 54 54"><rect x="6" y="16" width="42" height="30" rx="3" fill="#fff"/><rect x="20" y="8" width="14" height="10" fill="none" stroke="#fff" stroke-width="3"/><rect x="6" y="26" width="42" height="3" fill="var(--navy)"/></svg>CONTABILIDADE</div>
    <div class="service"><svg viewBox="0 0 54 54"><rect x="10" y="8" width="34" height="40" fill="#fff"/><rect x="14" y="12" width="26" height="8" fill="var(--navy)"/><rect x="14" y="24" width="26" height="8" fill="var(--navy)"/><rect x="14" y="36" width="26" height="8" fill="var(--navy)"/></svg>MOBÍLIA</div>
    <div class="service"><svg viewBox="0 0 54 54"><text x="27" y="44" text-anchor="middle" font-family="Montserrat,Arial,sans-serif" font-weight="800" font-size="44" fill="#fff">$</text></svg>REMESSAS<br>FINANCEIRAS</div>
    <div class="service"><svg viewBox="0 0 54 54"><rect x="4" y="12" width="46" height="30" rx="3" fill="#fff"/><circle cx="17" cy="25" r="5" fill="var(--navy)"/><rect x="26" y="20" width="18" height="3" fill="var(--navy)"/><rect x="26" y="28" width="14" height="3" fill="var(--navy)"/></svg>EB-5<br>(GREEN CARD)</div>
    <div class="service"><svg viewBox="0 0 54 54"><path d="M12 6h22l8 8v34H12z" fill="#fff"/><rect x="18" y="22" width="18" height="3" fill="var(--navy)"/><rect x="18" y="30" width="18" height="3" fill="var(--navy)"/><rect x="18" y="38" width="12" height="3" fill="var(--navy)"/></svg>DOCUMENTAÇÕES</div>
    <div class="service"><svg viewBox="0 0 54 54"><path d="M4 28L27 8l23 20h-6v20H34V34H20v14H10V28z" fill="#fff"/></svg>ADMINISTRAÇÃO<br>DE CASAS</div>
  </div>
</section>

<section class="specialist abs" role="img" aria-label="Vista noturna de cidade em tons escuros">
  <h2>DESEJA FALAR COM UM ESPECIALISTA?</h2>
  <div class="pill">AGENDAR ATENDIMENTO &nbsp;<svg width="18" height="18" viewBox="0 0 18 18"><rect x="2" y="3" width="14" height="13" rx="1" fill="none" stroke="#fff" stroke-width="2"/><rect x="2" y="3" width="14" height="4" fill="#fff"/></svg></div>
</section>

<h2 class="section-title abs" style="top:2050px">NOSSA GALERIA</h2>
<section class="gallery abs">
  <div class="tile" role="img" aria-label="Portal de entrada de condomínio com palmeiras" style="background:linear-gradient(180deg,#6aa6d8,#8db06a)"></div>
  <div class="tile" role="img" aria-label="Casa térrea ao entardecer" style="background:linear-gradient(180deg,#3a3432,#6d5a45)"></div>
  <div class="tile" role="img" aria-label="Clube com fonte iluminada ao anoitecer" style="background:linear-gradient(180deg,#2c3d6a,#8a7050)"></div>
  <div class="tile" role="img" aria-label="Clubhouse com palmeiras ao pôr do sol" style="background:linear-gradient(180deg,#4d6fa8,#b08a6c)"></div>
  <div class="tile" role="img" aria-label="Sala de cinema com poltronas" style="background:linear-gradient(180deg,#3a2a22,#7a5a3a)"></div>
  <div class="tile" role="img" aria-label="Piscina de resort com palmeiras" style="background:linear-gradient(180deg,#6ab0e0,#3a9ab8)"></div>
  <div class="tile" role="img" aria-label="Casa branca de dois andares" style="background:linear-gradient(180deg,#8cc0e8,#c8d0d8)"></div>
  <div class="tile" role="img" aria-label="Vista aérea de condomínio residencial" style="background:linear-gradient(180deg,#7aa0b8,#6e8c5a)"></div>
  <div class="tile" role="img" aria-label="Piscina coberta com espreguiçadeiras" style="background:linear-gradient(180deg,#4a5560,#3aa0b0)"></div>
  <div class="tile" role="img" aria-label="Área de piscina com espreguiçadeiras azuis" style="background:linear-gradient(180deg,#8fb8d8,#4a9cc0)"></div>
  <div class="tile" role="img" aria-label="Fachada de casa branca com jardim" style="background:linear-gradient(180deg,#7eb4e4,#d8dde2)"></div>
  <div class="tile" role="img" aria-label="Cozinha moderna branca" style="background:linear-gradient(180deg,#e8e8e8,#b8b8b8)"></div>
  <div class="tile" role="img" aria-label="Piscina ao ar livre com grade" style="background:linear-gradient(180deg,#4e5a48,#40a8c8)"></div>
  <div class="tile" role="img" aria-label="Casa branca com garagem" style="background:linear-gradient(180deg,#98c4ea,#c0c4c8)"></div>
  <div class="tile" role="img" aria-label="Casa iluminada ao anoitecer" style="background:linear-gradient(180deg,#2c4a88,#6a6a70)"></div>
  <div class="tile" role="img" aria-label="Placa de entrada de loteamento" style="background:linear-gradient(180deg,#6aa6da,#4a6a8a)"></div>
</section>
<div class="pill load-more abs">LOAD MORE</div>

<section class="plans abs">
  <h2>RECEBA PREÇOS E PLANTAS DOS IMÓVEIS</h2>
  <p>Tenha a sua disposição informações dos nossos imóveis.<br>Você terá uma lista sempre atualizada com nossos lançamentos e casas disponíveis.</p>
  <div class="pill">SOLICITE AQUI &nbsp;<svg width="14" height="10" viewBox="0 0 14 10"><path d="M0 5h12M8 1l4 4-4 4" stroke="var(--red)" stroke-width="2" fill="none"/></svg></div>
</section>

<section class="builder">
  <div class="builder-photo abs" role="img" aria-label="Fachada de casa em tons escuros"></div>
  <div class="builder-side abs"></div>
  <div class="builder-text abs">
    <h2>HALVORSEN</h2>
    <p>HALVORSEN é mais do que uma simples construtora imobiliária. É uma das maiores construtoras dos ESTADOS UNIDOS. O compromisso com a qualidade, valor e integridade é a base fundamental HALVORSEN. Os condomínios construídos pela HALVORSEN atendem a todos os estilos de vida.</p>
  </div>
  <div class="stats abs">
    <div class="stat">40+<br>CIDADES</div>
    <div class="stat">18<br>ESTADOS</div>
    <div class="stat">FUNDADA<br>EM 1954</div>
    <div class="stat">MAIS DE 600<small>CONDOMÍNIOS EM<br>CONSTRUÇÃO</small></div>
  </div>
</section>

<section class="help abs">
  <h3>Estamos aqui para ajudar você</h3>
  <h2>NO QUE VOCÊ PRECISAR</h2>
  <p>Não hesite em falar com um de nossos especialistas.</p>
</section>
<div class="input abs" style="left:258px;top:4225px;width:337px;height:57px">Nome Completo</div>
<div class="input abs" style="left:605px;top:4225px;width:337px;height:57px">eMail</div>
<div class="input abs" style="left:258px;top:4298px;width:684px;height:165px">Mensagem</div>
<div class="pill submit abs">MENSAGEM</div>

<footer class="site-footer abs">
  <div class="addr abs" style="left:100px;top:88px;width:360px">
    <div style="display:flex;gap:8px"><svg width="12" height="16" viewBox="0 0 12 16"><path d="M6 0a6 6 0 0 1 6 6c0 4-6 10-6 10S0 10 0 6a6 6 0 0 1 6-6z" fill="var(--green)"/><circle cx="6" cy="6" r="2" fill="#fff"/></svg><div><b>Rio de Janeiro</b><br>Centro Vela Azul, Av. das Gaivotas 120,<br>Loja 2, Rio de Janeiro - Brasil</div></div>
    <div style="display:flex;gap:8px;margin-top:12px"><svg width="12" height="16" viewBox="0 0 12 16"><path d="M6 0a6 6 0 0 1 6 6c0 4-6 10-6 10S0 10 0 6a6 6 0 0 1 6-6z" fill="var(--green)"/><circle cx="6" cy="6" r="2" fill="#fff"/></svg><div><b>Orlando</b><br>4410 Palm Harbor Road, Suite 210, Orlando, USA</div></div>
    <div style="display:flex;gap:8px;margin-top:12px;align-items:center"><svg width="14" height="10" viewBox="0 0 14 10"><rect width="14" height="10" rx="1" fill="var(--green)"/><path d="M0 0l7 6 7-6" stroke="#fff" fill="none"/></svg>contato@thecoralparlor.com</div>
  </div>
  <div class="brand abs" style="left:490px;top:98px;width:220px">
    <span style="font-size:38px">CORAL</span>
    <span style="font-size:18px;letter-spacing:8px;margin-top:6px">PARLOR</span>
  </div>
  <div class="abs" style="left:835px;top:80px">
    <div class="pill chat-badge" style="font-size:12px;padding:6px 14px">ChatLine +1 (555)010-4471</div>
    <div style="display:flex;gap:14px;margin-top:8px">
      <div class="phone-row"><i></i>+55 21 0000-4412</div>
      <div class="phone-row"><i class="us"></i>+1 (555)010-2298</div>
    </div>
    <div style="display:flex;gap:30px;margin-top:16px">
      <div class="cta"><i style="background:var(--pink)"></i>FALE COM UM<br>AGENTE</div>
      <div class="cta"><i style="background:var(--teal)"></i>AGENDE UMA<br>CONVERSA</div>
    </div>
  </div>
</footer>
<div class="legal abs">
  <span>© 2017 - THE CORAL PARLOR</span>
  <nav><span>HOME</span><span>IMÓVEIS</span><span>MAGAZINE</span><span>CONTATO</span><span>TERMS OF USE</span></nav>
</div>

</body>
</html>
```